Lina Kareem Haddad Desert Fragrances

All our perfumes are non-alcoholic and water based. We want to have a design that would have some Arabic calligraphy, arabesque etc. We would be the label theme u design for all our scents. Of course, the scent flavor would changed. We will also use the pattern on the packaging of the scent as well. Something along the lines of this brand: http://velmorescents.example/en/.
Label size: Length 6"; Height 5"

Target Market(s)

middle east (Kuwait, UAE, Saudi Arabia);

Requirements
Must have
• 1. Flavor Name (editable)
• 2. Quantity 240 ml / 100 ml (editable)
• 3. Flavor Description (editable. each flavor has its own unique description)
• 4. Logo (place where we can display our logo. Logo file submitted.)
• 5. Company Name (editable. I should be able to edit this field too.)
Nice to have
• Flavor name in English and Arabic. You don't have to do any translation. Just make a space for us so that we can type-in the Arabic name. It wud be good to place the Arabic flavor name right below the English one.
Should not have
• images of animals, people

```html
<!DOCTYPE html>
<html lang="en">
<head>
<meta charset="utf-8">
<title>Lina Kareem Haddad Desert Fragrances – Label Design</title>
<link href="https://fonts.googleapis.com/css2?family=Berkshire+Swash&family=Oswald:wght@500&family=Cardo&family=Nunito:wght@600&display=swap" rel="stylesheet">
<style>
  :root {
    --bg: #f1f1f1;
    --black: #0b0b0b;
    --gold: #d4ac2c;
    --gold-light: #f3dc7a;
    --gold-deep: #a47c17;
    --gold-panel: #e6c863;
    --navy: #1b2a78;
    --brown: #7a5420;
    --grey-title: #8e8e8e;
    --ink: #333333;
  }
  * { margin: 0; padding: 0; box-sizing: border-box; }
  html, body { width: 1200px; height: 960px; overflow: hidden; }
  body {
    background: linear-gradient(180deg, #f6f6f6 0%, #f3f3f3 60%, #e9e9e9 100%);
    position: relative;
    font-family: 'Cardo', serif;
  }
  .brand-block {
    position: absolute; top: 60px; right: 90px; width: 230px;
    text-align: center;
  }
  .brand-name {
    font-family: 'Nunito', sans-serif; font-weight: 600;
    font-size: 19px; color: var(--brown); line-height: 1.3;
  }
  .brand-mark {
    width: 14px; height: 14px; border-radius: 50%;
    background: var(--brown); display: inline-block; margin-bottom: 10px;
  }
  .sheet-title {
    font-family: 'Oswald', sans-serif; font-weight: 500;
    font-size: 30px; color: var(--grey-title); margin-top: 26px; letter-spacing: 0.5px;
  }
  .sheet-size { font-family: 'Nunito', sans-serif; font-size: 17px; color: var(--ink); }

  .labels {
    position: absolute; top: 380px; left: 110px;
    display: flex; gap: 60px;
  }
  .label {
    width: 360px; height: 300px; position: relative;
    display: flex; flex-direction: column; align-items: center;
  }
  .label--black { background: var(--black); }
  .label--gold {
    background: linear-gradient(90deg, var(--gold-deep) 0%, var(--gold-light) 45%, var(--gold) 75%, var(--gold-deep) 100%);
  }
  .top-rule { position: absolute; top: 10px; left: 0; right: 0; height: 5px; }
  .label--black .top-rule { background: linear-gradient(90deg, var(--gold-deep), var(--gold-light), var(--gold-deep)); }
  .label--gold .top-rule { background: var(--navy); height: 3px; top: 0; }

  .pattern-panel {
    margin-top: 42px; width: 150px; height: 150px; position: relative;
    display: flex; align-items: center; justify-content: center;
  }
  .label--black .pattern-panel { background: linear-gradient(135deg, #8a6a1a, #f0d468 45%, #b08a25); }
  .label--gold .pattern-panel { background: linear-gradient(135deg, #c9a438, #f7e59a 50%, #8f7a3a); }
  .logo-seal {
    width: 66px; height: 66px; border-radius: 50%; background: var(--black);
    display: flex; align-items: center; justify-content: center; text-align: center;
    font-family: 'Cardo', serif; font-size: 9px; line-height: 1.2; color: var(--gold);
    padding: 6px;
  }
  .flavor-name { font-family: 'Berkshire Swash', cursive; font-size: 22px; margin-top: 24px; }
  .label--black .flavor-name { color: var(--gold-light); }
  .label--gold .flavor-name { color: var(--navy); }
  .flavor-desc { font-size: 6.5px; text-align: center; line-height: 1.4; margin-top: 8px; width: 160px; }
  .label--black .flavor-desc { color: var(--gold-light); }
  .label--gold .flavor-desc { color: var(--navy); }
  .quantity { position: absolute; bottom: 16px; font-size: 8px; }
  .label--black .quantity { color: var(--gold-light); }
  .label--gold .quantity { color: var(--navy); }
</style>
</head>
<body>
  <div class="brand-block">
    <span class="brand-mark"></span>
    <div class="brand-name">Lina Kareem Haddad</div>
    <div class="sheet-title">LABLE DESIGN</div>
    <div class="sheet-size">Size: 6″ (w) x 5″ (h)</div>
  </div>

  <div class="labels">
    <section class="label label--black">
      <div class="top-rule"></div>
      <div class="pattern-panel" role="img" aria-label="Gold arabesque geometric star pattern">
        <div class="logo-seal">Lina Kareem Haddad</div>
      </div>
      <h2 class="flavor-name">Sandlewood</h2>
      <p class="flavor-desc">Lorem ipsum dolor sit amet, consectetuer adipiscing elit. Aenean commodo ligula eget dolor. Aenean massa.</p>
      <p class="quantity">240 ml &nbsp;℮&nbsp; 1.5 Fl.Oz</p>
    </section>

    <section class="label label--gold">
      <div class="top-rule"></div>
      <div class="pattern-panel" role="img" aria-label="Gold and navy arabesque geometric star pattern">
        <div class="logo-seal">Lina Kareem Haddad</div>
      </div>
      <h2 class="flavor-name">Sandlewood</h2>
      <p class="flavor-desc">Lorem ipsum dolor sit amet, consectetuer adipiscing elit. Aenean commodo ligula eget dolor. Aenean massa.</p>
      <p class="quantity">240 ml &nbsp;℮&nbsp; 1.5 Fl.Oz</p>
    </section>
  </div>
</body>
</html>
```